Business Card for Industrial Distributor

We need a business card design for an industrial distributor. We sell machine parts for the manufacturing and oil industry. We would like the cards to look clean and modern but with a touch of industry.

Our colors are blue/white.

Please feel free to visit our website www.krovelmint.com

Target Market(s)

mexican manufacturers in the automobile/aerospace industry

Industry/Entity Type

Industrial

Colors
ffffff
0555a3

```html
<!DOCTYPE html>
<html lang="en">
<head>
<meta charset="utf-8">
<title>Krovelmint Business Card</title>
<link rel="stylesheet" href="https://fonts.googleapis.com/css2?family=Open+Sans:wght@400;600;700&display=swap">
<style>
  :root {
    --stage: #000000;
    --paper: #f3f3f3;
    --brand-navy: #26339a;
    --brand-blue: #0555a3;
    --name-blue: #1b5aa8;
    --ink: #3e3e3e;
    --back-deep: #2448a6;
    --back-light: #1472c0;
    --mark: #1f63c4;
  }
  * { margin: 0; padding: 0; box-sizing: border-box; }
  html, body { width: 1200px; height: 900px; overflow: hidden; background: var(--stage); }
  body { position: relative; font-family: "Open Sans", Arial, sans-serif; }

  .card { position: absolute; top: 200px; width: 309px; height: 502px; overflow: hidden; }

  .card-front { left: 265px; background: var(--paper); border-radius: 70px 0 70px 0; }
  .card-back {
    left: 641px; border-radius: 0 70px 0 70px;
    background:
      radial-gradient(circle at 25% 15%, rgba(40,140,210,.55), transparent 30%),
      radial-gradient(circle at 75% 12%, rgba(40,140,210,.5), transparent 28%),
      radial-gradient(circle at 30% 45%, rgba(40,140,210,.45), transparent 26%),
      radial-gradient(circle at 80% 60%, rgba(40,140,210,.4), transparent 28%),
      linear-gradient(160deg, var(--back-deep), #2a56b0 50%, var(--back-deep));
  }

  .brand { position: absolute; left: 0; right: 0; text-align: center; }
  .brand-dot { display: block; margin: 0 auto; border-radius: 50%; background: radial-gradient(circle at 40% 35%, #3f8fe0, var(--mark) 55%, #173f95); }
  .brand-name { display: block; font-weight: 700; color: var(--brand-navy); letter-spacing: -0.5px; line-height: 1; }

  .card-front .brand { top: 52px; }
  .card-front .brand-dot { width: 74px; height: 74px; margin-left: 118px; }
  .card-front .brand-name { font-size: 42px; margin-top: 12px; }

  .card-back .brand { top: 296px; }
  .card-back .brand-dot { width: 82px; height: 82px; margin-left: 115px; }
  .card-back .brand-name { font-size: 46px; margin-top: 14px; color: #1e2f8f; }

  .contact { position: absolute; left: 27px; top: 326px; color: var(--ink); font-size: 13.5px; line-height: 16px; }
  .person-name { font-size: 17px; font-weight: 600; color: var(--name-blue); line-height: 22px; }
  .person-role { margin-top: 2px; }
  .address { margin-top: 18px; }
  .contact-lines { margin-top: 10px; list-style: none; }
  .contact-lines li { display: flex; align-items: center; gap: 6px; height: 19px; }
  .contact-lines svg { width: 10px; height: 10px; fill: var(--brand-blue); }
</style>
</head>
<body>
  <section class="card card-front">
    <div class="brand">
      <span class="brand-dot"></span>
      <span class="brand-name">Krovelmint</span>
    </div>
    <div class="contact">
      <p class="person-name">JOHN SMITH</p>
      <p class="person-role">Managing Director</p>
      <p class="address">1234, Address Goes Here<br>Country Name, 123456</p>
      <ul class="contact-lines">
        <li>
          <svg viewBox="0 0 10 10" aria-hidden="true"><path d="M1 3.5C1 2 2.5 1.5 5 1.5S9 2 9 3.5L7.5 4 6.8 3H3.2L2.5 4ZM2.5 5h5l1 3.5h-7Z"/></svg>
          <span>823-456-7890</span>
        </li>
        <li>
          <svg viewBox="0 0 10 10" aria-hidden="true"><path d="M0.5 2h9v6h-9Z M1 2.5 5 5.5 9 2.5" stroke="#f3f3f3" stroke-width="0.8"/></svg>
          <span>info@youremail.com</span>
        </li>
      </ul>
    </div>
  </section>

  <section class="card card-back">
    <div class="brand">
      <span class="brand-dot"></span>
      <span class="brand-name">Krovelmint</span>
    </div>
  </section>
</body>
</html>
```